Business cards for property management company

Need new business cards designed for our property management company and rental community, Blue Fern Commons. These cards will be primarily picked up by rental applicants.

May be single or double sided design.

I need cards for two different people, listed below. The design can be the same for both, and the only information that will be different is name and email address.

Industry/Entity Type

Property Management

Requirements
Must have
• US standard business card - 2''x3.5'' horizontal design.

1. Logo (attached). The text does not have to stay below the logo, but the card does need to say "Blue Fern Commons" somewhere on it (does not have to be same font as logo, but those fonts are Americana Extra Bold and BlackJack if needed).
2. Name: one with "Paula Whitcombe" and one with "Darrell Whitcombe"
3. Email address: one with "paula@bluefernhome.com" and one with "darrell@bluefernhome.com"
4. Web address: bluefernhome.com
5. Phone: 281.604.2218
6. Address: 1783 Wexford Lane, Porterfield, Texas 77812 (zip code may me omitted, at your discretion)
Should not have
• No rounded corners or special cuts.

No bevel, emboss or shadow effects.

As a note, please do not use our website as a basis for color or design schemes. We are working on a redesign, based around the new logo (attached to brief).

```html
<!DOCTYPE html>
<html lang="en">
<head>
<meta charset="utf-8">
<title>Blue Fern Commons – Paula Whitcombe</title>
<link rel="stylesheet" href="https://fonts.googleapis.com/css2?family=Advent+Pro:wght@500;600&family=Uncial+Antiqua&display=swap">
<style>
  :root {
    --sky-top: #5fe6fd;
    --sky-mid: #55dffb;
    --sea: #00d6fc;
    --edge: #2fd8fb;
    --foam: #e6fbff;
    --foam-fade: #98efff;
    --ink: #1a1f2a;
    --label: #1e5fd0;
    --name: #2306c8;
    --brand: #4a9a2e;
  }
  html, body {
    margin: 0;
    padding: 0;
    overflow: hidden;
    background: #ffffff;
  }
  .card {
    position: relative;
    width: 1200px;
    height: 686px;
    overflow: hidden;
    font-family: "Advent Pro", "Trebuchet MS", sans-serif;
  }
  .card__backdrop {
    position: absolute;
    inset: 0;
    width: 100%;
    height: 100%;
  }
  .brand {
    position: absolute;
    left: 14px;
    top: 150px;
    width: 240px;
    margin: 0;
    font-family: "Advent Pro", "Trebuchet MS", sans-serif;
    font-weight: 600;
    font-size: 38px;
    line-height: 1.05;
    color: var(--brand);
  }
  .contact {
    position: absolute;
    left: 638px;
    top: 18px;
    margin: 0;
    padding: 0;
    list-style: none;
    font-weight: 500;
    font-size: 33px;
    color: var(--ink);
  }
  .contact__item {
    height: 67.5px;
    line-height: 40px;
    white-space: nowrap;
  }
  .contact__label {
    color: var(--label);
  }
  .holder-name {
    position: absolute;
    left: 8px;
    top: 548px;
    margin: 0;
    font-family: "Uncial Antiqua", "Papyrus", fantasy;
    font-weight: 400;
    font-size: 76px;
    line-height: 1;
    color: var(--name);
    white-space: nowrap;
  }
</style>
</head>
<body>
<main class="card">
  <svg class="card__backdrop" viewBox="0 0 1050 600" preserveAspectRatio="none" aria-hidden="true">
    <defs>
      <linearGradient id="sky" x1="0" y1="0" x2="1" y2="1">
        <stop offset="0" stop-color="var(--sky-top)"/>
        <stop offset="1" stop-color="var(--sky-mid)"/>
      </linearGradient>
      <linearGradient id="foam" x1="0" y1="0" x2="1" y2="0">
        <stop offset="0" stop-color="var(--foam)"/>
        <stop offset="1" stop-color="var(--foam-fade)"/>
      </linearGradient>
    </defs>
    <rect class="sky" width="1050" height="600" fill="url(#sky)"/>
    <rect class="edge-strip" width="6" height="600" fill="var(--edge)"/>
    <path class="foam-band" d="M6 345 Q 500 430 1050 442 L1050 532 L980 530 Q 500 480 6 362 Z" fill="url(#foam)"/>
    <path class="sea-band" d="M0 362 L6 362 Q 500 480 980 530 L1050 532 L1050 600 L0 600 Z" fill="var(--sea)"/>
  </svg>

  <p class="brand">Blue Fern Commons</p>

  <ul class="contact">
    <li class="contact__item">1783 Wexford Lane, Porterfield, Texas</li>
    <li class="contact__item"><span class="contact__label">Phone:</span> 281 604 2218</li>
    <li class="contact__item"><span class="contact__label">E-mail:</span> paula@bluefernhome.com</li>
    <li class="contact__item"><span class="contact__label">Website:</span> www.bluefernhome.com</li>
  </ul>

  <h1 class="holder-name">Paula Whitcombe</h1>
</main>
</body>
</html>
```